TKR Website Overhaul. Complete new website look and function.

Need our website overhauled to be updated so it aligns better with our current cliental. We have competitors to compare to. The purpose of the site has changed and is no longer sales based. This site needs to qualify us and allow consultants and engineers to just discover our background and differentiators. I have attached a company profile from a recent project to provide a better idea. This profile is directed towards the specific project however so that would need to be edited out. Competitor websites that we would want to be comparable to would include: https://www.velmorbuild.com/ , https://tamblinconstruction.ca/ , https://www.pikeconstruction.ca/ , https://steadfastdiggers.com/ , https://www.lunacrestconstruction.ca/. These are all competitors so nothing can be directly copied. I have attached our logo's however I don't think they need to be directly used on the site or maybe they need to be changed to not include color etc. We need to have a more professional look and these colorful logos are hard to pull that off with other than maybe the all gold TKR prime contracting logo with a rich dark green background or something. Green has been our main color over the years and the leaf follows us as the core item in logos. Go with a gold leaf look or something. Our main focus is General Contracting (Prime Contracting) and civil construction. We are a home builder however we would do a second website for that so we don't want to include it. I don't mind a ton of generic civil and general contractor information etc on the site. I don't really need a portfolio of pictures showing on the site but job history etc is very common in the industry and that information can be found in the company profile attached. First Nation work is a big part of our portfolio but we have worked in mining, industrial, oil and gas as well. Municipal sewer and water is our main focus for civil construction though and is a big part of our First Nation work as well.

Industry/Entity Type

General Contractor and Civil Construction

Coding

Coded - Design and coding required

Number of Pages Required

5+ page

Font styles to use
Other font styles liked:
• A mix of Times New Roman, script and serif to create a very professional with a touch of elegance to match our leafed prime contractor logo.

Colors
00AB8E
00BBA5
67D7C9
C6EFE9
E9F9F6

Requirements
Must have
• A rich high end professional look. This company completes government work and is often looked at by executives. A menu that includes About, Our Work, Methodology, Join Our Team and Contact
Nice to have
• Some generic general pictures of municipal underground water work and general contractor building work. I am looking for a rich green darker greens where it matters but with more real world feel overall. So images and movement is good. Civil underground water and sewer, storm water, retention ponds, and process plant and electrical (such as water treatment plants), background imagery is good to have. I like to have things faded out in the background more than in your face.
Should not have
• brighter colors.

```html
<!DOCTYPE html>
<html lang="en">
<head>
<meta charset="utf-8">
<title>TKR Prime Contracting</title>
<link href="https://fonts.googleapis.com/css2?family=Tinos:wght@400;700&family=Outfit:wght@300;400;500&display=swap" rel="stylesheet">
<style>
:root{
  --gold:#c9992f;
  --green:#1a9a5a;
  --forest:#03190f;
  --ink:#111111;
  --muted:#555555;
  --line:#e6e6e6;
  --white:#ffffff;
  --serif:"Tinos","Times New Roman",serif;
  --sans:"Outfit",Arial,sans-serif;
}
*{box-sizing:border-box;margin:0;padding:0}
html,body{width:1200px;height:3406px;overflow:hidden;background:var(--white)}
body{position:relative;font-family:var(--sans);color:var(--ink)}
.abs{position:absolute}
.center{left:0;width:1200px;text-align:center}
.serif-title{font-family:var(--serif);font-weight:700;text-transform:uppercase;letter-spacing:1.5px}
.rule{position:absolute;left:574px;width:52px;height:4px;background:var(--green)}
.btn{position:absolute;display:flex;align-items:center;justify-content:center;background:var(--gold);color:var(--white);font-size:14px;font-weight:500}

/* hero */
.hero-band{position:absolute;top:0;left:0;width:1200px;height:751px;background:var(--green);clip-path:polygon(0 654px,600px 751px,1200px 654px,1200px 640px,0 640px)}
.hero-photo{position:absolute;top:0;left:0;width:1200px;height:740px;clip-path:polygon(0 0,1200px 0,1200px 654px,600px 740px,0 654px);
  background:radial-gradient(ellipse at 32% 22%,#8a6a3a 0%,#4a3a28 22%,transparent 50%),linear-gradient(180deg,#2c2a26 0%,#3b3227 35%,#241f1a 70%,#15130f 100%)}
.hero-photo::after{content:"";position:absolute;inset:0;background:rgba(0,0,0,.35)}
.site-header{position:absolute;top:0;left:0;width:1200px;height:93px;background:rgba(14,58,38,.88)}
.brand{position:absolute;font-family:var(--serif);font-weight:700;color:var(--gold);display:flex;align-items:center;gap:10px;white-space:nowrap}
.brand .mark{width:14px;height:14px;background:var(--gold)}
.nav-item{position:absolute;font-size:13px;line-height:16px;color:var(--white);white-space:nowrap}
.main-nav .nav-item{top:39px}
.footer-nav .nav-item{top:3222px}

.hero-title{top:222px;font-size:52px;line-height:54px;color:var(--white)}
.hero-sub{top:341px;font-size:13px;line-height:19px;color:var(--white);font-weight:500}

.section-title{font-size:38px;line-height:42px;color:var(--ink)}
.lede{font-size:13px;line-height:19px;color:var(--muted)}

.card-photo{position:absolute;top:1308px;width:334px;height:262px}
.card-title{position:absolute;top:1590px;width:334px;text-align:center;font-family:var(--serif);font-weight:700;font-size:14px;letter-spacing:1px}
.card-text{position:absolute;top:1614px;width:334px;text-align:center;font-size:12.5px;line-height:19px;color:var(--muted)}

.approach{position:absolute;top:1822px;left:0;width:1200px;height:314px;background:var(--forest)}
.step-num{position:absolute;top:147px;width:54px;height:51px;background:var(--gold);color:var(--white);font-family:var(--serif);font-weight:700;font-size:24px;display:flex;align-items:center;justify-content:center}
.step-label{position:absolute;top:212px;width:180px;text-align:center;color:var(--white);font-size:12.5px;line-height:19px}
.step-link{position:absolute;top:172px;height:0;border-top:1px dashed var(--gold)}

.project-table{position:absolute;top:2372px;left:74px;width:1050px;border-collapse:collapse}
.project-table th{font-family:var(--serif);font-weight:700;color:var(--gold);font-size:15px;letter-spacing:1px;text-align:left;height:77px;border-bottom:1px solid var(--line)}
.project-table td{font-family:var(--serif);font-weight:700;font-size:15px;letter-spacing:1px;text-align:left;border-bottom:1px solid var(--line)}
.project-table td.deliverable{font-family:var(--sans);font-weight:400;font-size:12px;line-height:19px;color:var(--muted);letter-spacing:0}
.project-table th:first-child,.project-table td:first-child{padding-left:23px;width:395px}
.project-table th:nth-child(2),.project-table td:nth-child(2){width:335px}
.project-table td:last-child{padding-right:20px}

.footer-green{position:absolute;top:3030px;left:0;width:1200px;height:376px;background:var(--green);clip-path:polygon(0 100px,600px 0,1200px 100px,1200px 376px,0 376px)}
.footer-black{position:absolute;top:3043px;left:0;width:1200px;height:363px;background:#000;clip-path:polygon(0 87px,600px 0,1200px 87px,1200px 363px,0 363px)}
.contact-line{position:absolute;top:3265px;right:75px;display:flex;align-items:center;gap:10px;color:var(--white);font-size:12px;white-space:nowrap}
.contact-icon{width:35px;height:35px;border-radius:50%;background:var(--gold);display:flex;align-items:center;justify-content:center}
.footer-rule{position:absolute;top:3338px;left:75px;width:1050px;height:1px;background:#333}
.legal{position:absolute;top:3362px;color:var(--white);font-size:12px}
</style>
</head>
<body>

<div class="hero-band"></div>
<div class="hero-photo" role="img" aria-label="Dusk view over a city building site with a tower crane and road lights"></div>

<header class="site-header">
  <div class="brand" style="left:75px;top:28px;font-size:28px;line-height:36px;"><span class="mark"></span>TKR Construction</div>
  <nav class="main-nav">
    <span class="nav-item" style="left:493px">Home</span>
    <span class="nav-item" style="left:549px">|</span>
    <span class="nav-item" style="left:574px">About Us</span>
    <span class="nav-item" style="left:648px">|</span>
    <span class="nav-item" style="left:673px">Our Work</span>
    <span class="nav-item" style="left:750px">|</span>
    <span class="nav-item" style="left:775px">Methodology</span>
    <span class="nav-item" style="left:871px">|</span>
    <span class="nav-item" style="left:896px">Join Our Team</span>
  </nav>
  <div class="btn" style="left:1002px;top:27px;width:123px;height:38px;font-size:13px;">Contact Us</div>
</header>

<h1 class="abs center serif-title hero-title">Bridging Excellence in Civil<br>&amp; Prime Contracting.</h1>
<p class="abs center hero-sub">Partnering with Government, Industry, and First Nations to deliver sustainable infrastructure<br>for the future.</p>
<div class="btn" style="left:498px;top:396px;width:204px;height:38px;">Explore Our Methodology</div>

<svg class="abs" style="left:588px;top:668px" width="24" height="42" viewBox="0 0 24 42" aria-hidden="true">
  <path d="M12 1V40M2 30l10 10 10-10" fill="none" stroke="#fff" stroke-width="2"/>
</svg>

<div class="abs" style="left:590px;top:838px;width:20px;height:20px;background:var(--gold);"></div>
<h2 class="abs center serif-title section-title" style="top:890px;line-height:41px;">Proven Expertise. Government<br>Trusted.</h2>
<div class="rule" style="top:987px"></div>
<p class="abs center lede" style="top:1006px;">TKR Prime Contracting is more than a general contractor. We specialize in complex civil construction, municipal water<br>systems, and industrial infrastructure. Our focus is on qualifying for elite projects through high-end methodology<br>and a legacy of trust with government executives and mining partners.</p>
<div class="btn" style="left:542px;top:1080px;width:116px;height:38px;">Read More</div>

<h2 class="abs center serif-title section-title" style="top:1215px;">Our Services</h2>
<div class="rule" style="top:1267px"></div>

<div class="card-photo" style="left:77px;background:linear-gradient(180deg,#9fb0c2 0%,#6d7886 45%,#3b3f47 100%);" role="img" aria-label="City rail yard with dense buildings at dusk"></div>
<div class="card-photo" style="left:433px;background:linear-gradient(180deg,#d9a458 0%,#c0843e 50%,#5a3a22 100%);" role="img" aria-label="Site workers in safety gear on rebar deck with crane at sunset"></div>
<div class="card-photo" style="left:790px;background:linear-gradient(135deg,#f2f2f0 0%,#dcdcd8 55%,#b9bcc4 100%);" role="img" aria-label="Hard hat on construction plans on a desk"></div>

<h3 class="card-title" style="left:77px;">MUNICIPAL INFRASTRUCTURE</h3>
<p class="card-text" style="left:77px;">Expertise in sewer, water lines, and<br>storm-water management.</p>
<h3 class="card-title" style="left:433px;">CIVIL CONSTRUCTION</h3>
<p class="card-text" style="left:433px;">Heavy earthworks, retention ponds,<br>and site preparation.</p>
<h3 class="card-title" style="left:790px;">FIRST NATIONS PARTNERSHIPS</h3>
<p class="card-text" style="left:790px;">A core part of our portfolio, delivering vital<br>infrastructure to indigenous.</p>

<svg class="abs" style="left:551px;top:1697px" width="96" height="22" viewBox="0 0 96 22" aria-label="Previous and next">
  <path d="M41 11H2M11 2L2 11l9 9" fill="none" stroke="#1a9a5a" stroke-width="2"/>
  <path d="M55 11h39M85 2l9 9-9 9" fill="none" stroke="#c9992f" stroke-width="2"/>
</svg>

<section class="approach">
  <h2 class="abs center serif-title section-title" style="top:54px;color:var(--white);">The TKR Approach.</h2>
  <div class="rule" style="top:105px"></div>
  <div class="step-link" style="left:266px;width:185px"></div>
  <div class="step-link" style="left:505px;width:186px"></div>
  <div class="step-link" style="left:745px;width:184px"></div>
  <div class="step-num" style="left:212px">01</div>
  <div class="step-num" style="left:451px">02</div>
  <div class="step-num" style="left:691px">03</div>
  <div class="step-num" style="left:929px">04</div>
  <p class="step-label" style="left:149px">Strategic Planning And<br>Execution.</p>
  <p class="step-label" style="left:388px">Environmental Steward<br>ship</p>
  <p class="step-label" style="left:628px">Government &amp; Safety<br>Compliance.</p>
  <p class="step-label" style="left:866px">Indigenous Engagement &amp;<br>Collaboration.</p>
</section>

<h2 class="abs center serif-title section-title" style="top:2235px;">Selected Project History.</h2>
<div class="rule" style="top:2286px"></div>
<p class="abs center lede" style="top:2309px;">Ek professional table ya list jahan aapke pichle bade projects (Mining, Oil &amp; Gas, Municipal)<br>ke naam aur unki types likhi hon.</p>

<table class="project-table">
  <thead>
    <tr><th>PROJECT CATEGORY</th><th>SECTOR</th><th>PRIMARY DELIVERABLES</th></tr>
  </thead>
  <tbody>
    <tr style="height:96px"><td>MUNICIPAL SEWER &amp; WATER</td><td>MUNICIPAL / GOVERNMENT</td><td class="deliverable">Deep bury utility installation, main line extensions,<br>and lift station integration.</td></tr>
    <tr style="height:89px"><td>FIRST NATION INFRASTRUCTURE</td><td>INDIGENOUS COMMUNITIES</td><td class="deliverable">Community water distribution systems &amp; sustaina<br>ble storm-water management.</td></tr>
    <tr style="height:98px"><td>MINING SITE DEVELOPMENT</td><td>INDUSTRIAL / MINING</td><td class="deliverable">Heavy earthworks, retention pond construction,<br>and site access road development.</td></tr>
    <tr style="height:91px"><td>OIL &amp; GAS PROCESS SUPPORT</td><td>ENERGY / OIL &amp; GAS</td><td class="deliverable">Facility site preparation, electrical process plant<br>civil works, and containment systems.</td></tr>
    <tr style="height:95px"><td>WATER TREATMENT FACILITIES</td><td>MUNICIPAL / PROCESS</td><td class="deliverable">Structural civil work for treatment plants and<br>complex underground piping networks.</td></tr>
  </tbody>
</table>

<footer>
  <div class="footer-green"></div>
  <div class="footer-black"></div>
  <div class="brand" style="left:75px;top:3237px;font-size:36px;line-height:44px;"><span class="mark" style="width:18px;height:18px"></span>TKR Construction</div>
  <nav class="footer-nav">
    <span class="nav-item" style="left:640px">Home</span>
    <span class="nav-item" style="left:695px">|</span>
    <span class="nav-item" style="left:721px">About Us</span>
    <span class="nav-item" style="left:794px">|</span>
    <span class="nav-item" style="left:820px">Our Work</span>
    <span class="nav-item" style="left:896px">|</span>
    <span class="nav-item" style="left:921px">Methodology</span>
    <span class="nav-item" style="left:1018px">|</span>
    <span class="nav-item" style="left:1043px">Join Our Team</span>
  </nav>
  <div class="contact-line">
    <span class="contact-icon"><svg width="16" height="16" viewBox="0 0 24 24" aria-hidden="true"><path fill="#fff" d="M6.6 10.8a15.1 15.1 0 0 0 6.6 6.6l2.2-2.2c.3-.3.7-.4 1-.2 1.1.4 2.3.6 3.6.6.6 0 1 .4 1 1V20c0 .6-.4 1-1 1C10.6 21 3 13.4 3 4c0-.6.4-1 1-1h3.5c.6 0 1 .4 1 1 0 1.3.2 2.5.6 3.6.1.3 0 .7-.2 1z"/></svg></span>
    <span>(403) 555 0187</span>
    <span style="width:20px"></span>
    <span class="contact-icon"><svg width="14" height="18" viewBox="0 0 24 30" aria-hidden="true"><path fill="#fff" d="M12 0C5.4 0 0 5.2 0 11.7 0 20.5 12 30 12 30s12-9.5 12-18.3C24 5.2 18.6 0 12 0zm0 16a4.5 4.5 0 1 1 0-9 4.5 4.5 0 0 1 0 9z"/></svg></span>
    <span>Tallridge Holdings Ltd. Box 210 Cochrane Alberta T4C0A1</span>
  </div>
  <div class="footer-rule"></div>
  <p class="legal" style="left:75px;">© 2026 TKR Prime Contracting. All Rights Reserved.</p>
  <p class="legal" style="right:75px;">Privacy Policy.</p>
</footer>

</body>
</html>
```